Report presentation for measurement or inline reports

First page of report. Our inline reporting will come in a maintenance map. We want a modern first page and a real eye-catcher for a new company based in the Netherlands called: RTP Luchtregeling B.V. We are a service company witch measures, balances and give advices at indoor climate HVAC installations. We would like to see designs that use the color blue. We deliver our services to different buildings: Hospitals, atractions, officebuildings, government buildings, swimming pools and schools. Our website: www.rtpl.nl
Updates

Can you all add the new logo please. The companyname is RTP Luchtregeling B.V.. In witch format can i retrieve the design?

Industry/Entity Type

It Company

Colors
0255a3
3176b5
85abd2
cedeed
eaf1f7
ffffff

Requirements
Must have
• Projectname; projectplace; Inline or measure report; date; logo; companyname. it must be easy printable so not to much colours.
• The companyname is: RTP Luchtregeling B.V.. Please add the name. A new logo is updated.
Nice to have
• Maybe some pictures from hvac installations, buildings or measure

```html
<!DOCTYPE html>
<html lang="en">
<head>
<meta charset="utf-8">
<title>Inline Reporting – RTP Luchtregeling B.V.</title>
<link rel="stylesheet" href="https://fonts.googleapis.com/css2?family=Fira+Mono:wght@400&family=Barlow:wght@600&display=swap">
<style>
  :root {
    --stage: #d9d9d9;
    --cover-dark: #2b2c2e;
    --cover-mid: #3c3d40;
    --accent-blue: #0d9ad6;
    --paper-white: #ffffff;
    --band-white: #e9eaec;
    --logo-blue: #0255a3;
  }
  * { margin: 0; padding: 0; box-sizing: border-box; }
  html, body {
    width: 1200px;
    height: 1200px;
    overflow: hidden;
    background: var(--stage);
  }
  .report-cover {
    position: absolute;
    left: 175px;
    top: 0;
    width: 849px;
    height: 1200px;
    overflow: hidden;
    color: var(--paper-white);
  }
  .cover-photo {
    position: absolute;
    inset: 0;
    background:
      linear-gradient(90deg, rgba(0,0,0,0.25) 0%, rgba(0,0,0,0) 30%, rgba(0,0,0,0) 70%, rgba(0,0,0,0.2) 100%),
      linear-gradient(180deg, var(--cover-dark) 0%, var(--cover-mid) 55%, var(--cover-dark) 100%);
  }
  .cover-accents {
    position: absolute;
    inset: 0;
    width: 100%;
    height: 100%;
  }
  .report-title {
    position: absolute;
    left: 56px;
    top: 378px;
    font-family: "Fira Mono", monospace;
    font-weight: 400;
    font-size: 112px;
    line-height: 100px;
    letter-spacing: -3px;
  }
  .report-title .title-type { display: block; color: var(--accent-blue); }
  .report-title .title-kind { display: block; color: var(--paper-white); }
  .project-line {
    position: absolute;
    left: 53px;
    top: 652px;
    font-family: "Barlow", sans-serif;
    font-weight: 600;
    font-size: 40px;
    line-height: 44px;
  }
  .measurement-meta {
    position: absolute;
    left: 54px;
    top: 756px;
    font-family: "Barlow", sans-serif;
    font-weight: 600;
    font-size: 23px;
    line-height: 29px;
    letter-spacing: 0.3px;
  }
  .company-mark {
    position: absolute;
    left: 690px;
    top: 1040px;
    width: 108px;
    height: 108px;
    background: var(--paper-white);
    display: flex;
    align-items: center;
    justify-content: center;
    text-align: center;
    font-family: "Barlow", sans-serif;
    font-weight: 600;
    font-size: 15px;
    line-height: 18px;
    color: var(--logo-blue);
  }
</style>
</head>
<body>
  <main class="report-cover">
    <div class="cover-photo" role="img" aria-label="Dark photograph of galvanised spiral HVAC ducts and pipework"></div>

    <svg class="cover-accents" viewBox="0 0 817 1155" preserveAspectRatio="none" aria-hidden="true">
      <polygon points="422,0 428,0 817,374 817,528" fill="var(--band-white)"/>
      <polygon points="434,0 528,0 817,250 817,356" fill="var(--accent-blue)"/>
    </svg>

    <h1 class="report-title">
      <span class="title-type">Inline</span>
      <span class="title-kind">Reporting</span>
    </h1>

    <p class="project-line">Testproject in Testplace</p>

    <p class="measurement-meta">Measured by RTP<br>Luchtregeling<br>B.V. on 1-5-2017</p>

    <div class="company-mark">RTP<br>Solutions</div>
  </main>
</body>
</html>
```